Business Card Design

We have recently seen two business cards that caught our attention and think the designs would work for us. We are an accounting firm that serves small businesses in a variety of industries. Attached are the two business card that inspired us along with very rough layouts. We would like to see a professional layout using our company information.

Industry/Entity Type

Accounting

Contact Information for Business Card

Company Name - Porter Lyle
Address - 4120 Marbury Lane, Suite 310, Houston, TX 77058
713-555-0186 - Main
281-555-0143 - Fax

Team Member Names, emails and phone numbers (see attachment)

```html
<!DOCTYPE html>
<html lang="en">
<head>
<meta charset="utf-8">
<title>Porter Lyle — Business Card</title>
<link rel="stylesheet" href="https://fonts.googleapis.com/css2?family=Open+Sans:wght@400;600&display=swap">
<style>
  :root {
    --backdrop: #b4b4b4;
    --card: #ffffff;
    --ink: #111111;
    --muted: #9a9a9a;
    --rule: #1a1a1a;
  }
  * { box-sizing: border-box; margin: 0; padding: 0; }
  html, body {
    width: 1200px;
    height: 900px;
    overflow: hidden;
    background: var(--backdrop);
    font-family: "Open Sans", Arial, sans-serif;
  }
  .stage {
    width: 1200px;
    height: 900px;
    display: flex;
    align-items: center;
    justify-content: center;
  }
  .business-card {
    position: relative;
    width: 980px;
    height: 560px;
    background: var(--card);
    border-radius: 44px;
    display: flex;
    align-items: center;
  }
  .brand {
    width: 500px;
    display: flex;
    align-items: center;
    justify-content: center;
    gap: 22px;
    padding-left: 30px;
  }
  .brand-mark {
    width: 34px;
    height: 34px;
    background: var(--ink);
  }
  .brand-name {
    font-size: 52px;
    font-weight: 600;
    color: var(--ink);
    letter-spacing: 0.5px;
    white-space: nowrap;
  }
  .divider {
    width: 2px;
    height: 330px;
    background: var(--rule);
  }
  .contact {
    padding-left: 80px;
    color: var(--ink);
  }
  .person-name {
    font-size: 29px;
    font-weight: 600;
    line-height: 1.2;
  }
  .person-title {
    font-size: 20px;
    color: var(--muted);
    margin-top: 4px;
  }
  .details {
    margin-top: 62px;
    font-size: 20px;
    line-height: 1.4;
    border-collapse: collapse;
  }
  .details td { padding: 0; }
  .details .label { width: 80px; }
  .address {
    font-size: 20px;
    line-height: 1.4;
  }
</style>
</head>
<body>
<main class="stage">
  <article class="business-card">
    <section class="brand">
      <span class="brand-mark" aria-hidden="true"></span>
      <span class="brand-name">Porter Lyle</span>
    </section>
    <div class="divider" aria-hidden="true"></div>
    <section class="contact">
      <h1 class="person-name">Marissa Dalton</h1>
      <p class="person-title">Account Manager</p>
      <table class="details">
        <tr><td class="label">Direct:</td><td>713-555-0172</td></tr>
        <tr><td class="label">Mobile:</td><td>832-555-0129</td></tr>
        <tr><td class="label">Main:</td><td>713-555-0186</td></tr>
        <tr><td class="label">Fax:</td><td>281-555-0143</td></tr>
      </table>
      <p class="address">4120 Marbury Lane, Suite 310<br>Houston, TX 77058</p>
    </section>
  </article>
</main>
</body>
</html>
```